Resume redesign

I'm a researcher who works with web design companies. I'm updating my resume but want more than the standard black and white wall of text. The content is updated, what I need is a design to make it readable, or in the words of my friend the hiring manager 'it needs to have high scan value'. It has to strike some balance between professionalism and readability.

There are two versions of my resume attached. I'm willing to cut some information if needed or reword things to simplify them. It would be great if it could be cut down to 2 pages, although this may require eliminating the publications section (which is fine).

```html
<!DOCTYPE html>
<html lang="en">
<head>
<meta charset="utf-8">
<title>Daniel Crowe – Research Consultant</title>
<link rel="stylesheet" href="https://fonts.googleapis.com/css2?family=Didact+Gothic&family=Maven+Pro:wght@400;500&display=swap">
<style>
  :root {
    --blue: #1f7fcb;
    --dark: #3b3b3b;
    --text: #8a8a8a;
    --ink: #2b2b2b;
    --paper: #ffffff;
    --rule: #9a9a9a;
  }
  * { margin: 0; padding: 0; box-sizing: border-box; }
  html, body { width: 848px; height: 1200px; overflow: hidden; background: var(--paper); }
  body { position: relative; font-family: "Didact Gothic", sans-serif; color: var(--text); }
  .abs { position: absolute; }

  .contact-box { left: 90px; top: 66px; width: 371px; height: 93px; background: var(--blue); color: #fff; padding: 20px 0 0 18px; font-family: "Maven Pro", sans-serif; font-size: 12.5px; }
  .contact-row { display: flex; align-items: center; gap: 6px; margin-bottom: 9px; white-space: nowrap; }
  .contact-row svg { flex: none; }
  .contact-row .gap { width: 8px; }

  .portrait { left: 496px; top: 70px; width: 56px; height: 86px; border: 3px solid #fff; box-shadow: 0 0 3px rgba(0,0,0,.35); background: linear-gradient(160deg, #6f7f5c, #8a6d58 55%, #4a4f44); }
  .portrait { width: 56px; }

  .identity { left: 612px; top: 100px; }
  .identity .name { font-family: "Maven Pro", sans-serif; font-size: 23px; color: var(--blue); line-height: 1; letter-spacing: -0.3px; }
  .identity .role { font-size: 10px; letter-spacing: 1.8px; color: var(--text); line-height: 1.25; margin-top: 3px; }

  .dash { border-top: 1px dashed var(--rule); height: 0; }

  .head-bar { height: 60px; display: flex; align-items: center; padding-left: 10px; font-family: "Maven Pro", sans-serif; font-size: 18px; color: #fff; }
  .head-bar.blue { left: 90px; top: 181px; width: 383px; background: var(--blue); }
  .head-bar.dark { left: 490px; top: 181px; width: 287px; background: var(--dark); }

  .summary-icon { left: 90px; top: 250px; width: 41px; height: 41px; background: var(--blue); display: flex; align-items: center; justify-content: center; }
  .summary { left: 151px; top: 260px; width: 315px; font-size: 14.5px; line-height: 17.6px; letter-spacing: 0.45px; text-align: justify; }
  .expertise { left: 498px; top: 260px; width: 271px; font-size: 12.4px; line-height: 14.7px; letter-spacing: 0.35px; text-align: justify; text-transform: uppercase; }

  .section-label { left: 90px; top: 582px; font-family: "Maven Pro", sans-serif; font-size: 11.5px; color: var(--ink); }
  .section-label .dates { color: var(--blue); font-size: 14px; margin-left: 8px; }

  .company-band { left: 81px; top: 613px; width: 696px; height: 78px; background: var(--dark); color: #fff; }
  .company-band .company { position: absolute; left: 9px; top: 30px; font-family: "Maven Pro", sans-serif; font-size: 15px; }
  .company-band .about { position: absolute; left: 357px; top: 14px; width: 310px; font-size: 12px; line-height: 14.5px; color: #c8c8c8; }

  .role-icon { left: 111px; top: 713px; }
  .role-title { left: 151px; top: 709px; font-family: "Maven Pro", sans-serif; font-size: 18.5px; color: var(--ink); }
  .role-desc { left: 151px; top: 731px; width: 620px; font-size: 12px; line-height: 14.5px; }
  .selected { left: 151px; top: 788px; font-size: 14px; color: #555; }

  .project-title { left: 151px; font-family: "Maven Pro", sans-serif; font-size: 16px; color: var(--ink); }
  .project-desc { left: 210px; width: 300px; font-size: 12px; line-height: 14.7px; }
  .methods { left: 549px; width: 220px; text-align: right; font-size: 12px; line-height: 14.7px; }
  .methods b { font-weight: normal; color: var(--ink); }
</style>
</head>
<body>

<div class="abs contact-box">
  <div class="contact-row">
    <svg width="17" height="17" viewBox="0 0 24 24" fill="none" stroke="#fff" stroke-width="2"><path d="M5 3h4l2 5-3 2a11 11 0 0 0 6 6l2-3 5 2v4a2 2 0 0 1-2 2A17 17 0 0 1 3 5a2 2 0 0 1 2-2z"/></svg>
    <span>(+555) 014-2273</span>
    <span class="gap"></span>
    <svg width="17" height="15" viewBox="0 0 24 20" fill="none" stroke="#fff" stroke-width="2"><rect x="2" y="2" width="20" height="16"/><path d="M2 3l10 8 10-8"/></svg>
    <span>daniel@tallpathresearch.com</span>
  </div>
  <div class="contact-row">
    <svg width="17" height="16" viewBox="0 0 24 22" fill="none" stroke="#fff" stroke-width="2"><path d="M2 11L12 2l10 9"/><path d="M5 9v11h14V9"/><path d="M10 20v-6h4v6"/></svg>
    <span>4120 Elm Ridge Road, Millbrook, FL 32000</span>
  </div>
</div>

<div class="abs portrait" role="img" aria-label="Portrait photograph of the researcher"></div>

<div class="abs identity">
  <div class="name">DANIEL CROWE</div>
  <div class="role">RESEARCH CONSULTANT<br>PHD, MBA</div>
</div>

<div class="abs dash" style="left:90px;top:169px;width:669px;"></div>

<div class="abs head-bar blue">RESEARCH CONSULTANT</div>
<div class="abs head-bar dark">Areas of expertise</div>

<div class="abs summary-icon">
  <svg width="24" height="24" viewBox="0 0 24 24" fill="none" stroke="#fff" stroke-width="1.8"><path d="M5 4h14l2 12H3z"/><path d="M3 16v4h18v-4"/><path d="M8 16a4 3 0 0 0 8 0"/></svg>
</div>

<p class="abs summary">Forward-thinking and dynamic Senior Research Consultant with experience leading targeted research strategies and data collection initiatives to drive project success and reduce spending. Expert communicator who leverages strong research acumen to obtain key customer insight; collect and analyze data; and provide accurate primary and secondary findings to deliver value-enhancing recommendations across major, multimillion dollar projects with organizations including Northline Telecom, Crestway Pharmacy, Vantor Computing, and Quillmoor Bank. Expertise in developing customized and detailed research solutions to fit the scope of a range of projects and ensure accurate and profitable results.</p>

<p class="abs expertise">Research design – quantitative &amp; qualitative data collection – primary &amp; secondary research – statistical analysis – ethnography matrix analysis – structured cultural domain analysis – text analysis – social media analysis – multivariate analysis strategic planning– non-parametric &amp; categorical analysis – online &amp; on-site interviews – panel management –usability testing observational testing – survey management – focus groups – cognitive anthropology –taxonomic research – Tabvex – Statquill – Qorvane.</p>

<div class="abs dash" style="left:90px;top:571px;width:669px;"></div>

<div class="abs section-label">PROFESSIONAL EXPERIENCE<span class="dates">2007 TO PRESENT</span></div>

<div class="abs company-band">
  <div class="company">TALL PATH RESEARCH, LLC. _ MILLBROOK, FL</div>
  <div class="about">Boutique research firm providing customized solutions around consumer behavior, segmentation, and cultural models.</div>
</div>

<svg class="abs role-icon" width="15" height="15" viewBox="0 0 16 16"><circle cx="8" cy="8" r="8" fill="#8d8d8d"/><path d="M8 4v8M4 8h8" stroke="#fff" stroke-width="2"/></svg>
<div class="abs role-title">PRINCIPLE RESEARCHER</div>
<p class="abs role-desc">Design and implement effective, top-tier research design for a range of projects and industries. Directly interface with clients to communicate research processes and findings while collecting and analyzing appropriate types of data to recommend easily understood, actionable, and highly customized solutions and results.</p>

<div class="abs selected">Selected projects:</div>

<div class="abs project-title" style="top:806px;">Journal of Applied Lab Science</div>
<p class="abs project-desc" style="top:826px;">Project to understand readership segmentation and the utilization of both print and online versions of the publication. Implemented online survey to collect data from 1.6K+ respondents.</p>
<p class="abs methods" style="top:832px;"><b>Methods:</b> Survey design, sampling, web survey programming, quantitative data analysis, multivariate analysis.</p>

<div class="abs project-title" style="top:899px;">Lumen Electronics</div>
<p class="abs project-desc" style="top:919px;">Designed and moderated usability testing in pre-launch development test for a new television at Lumen Electronics. Analyzed recordings for patterns of issues among participants and why issues were significant to users. Suggested solutions to alleviate all problems.</p>
<p class="abs methods" style="top:939px;"><b>Methods:</b> Usability test moderation, transcript analysis.</p>

<div class="abs project-title" style="top:1006px;">Regional Utility Company</div>
<p class="abs project-desc" style="top:1026px;">Developed research project in coordination with MRU to examine apartment owner infrastructure upgrades to reduce the use of utilities. Moderated two focus groups and directly presented findings to MRU.</p>
<p class="abs methods" style="top:1040px;"><b>Methods:</b> Focus group moderation, text analysis.</p>

</body>
</html>
```